Word document template for sales proposals

I am after a template that is simple but impactful. Use of colour to be limited but some for impact would be good. The proposals are for use in the professional technical field.

```html
<!DOCTYPE html>
<html lang="en">
<head>
<meta charset="UTF-8">
<title>Sales Proposal Template</title>
<link rel="stylesheet" href="https://fonts.googleapis.com/css2?family=Poppins:wght@700&family=Source+Sans+3:wght@400&display=swap">
<style>
  :root {
    --ink: #1a1a1a;
    --accent-blue: #00aeef;
    --accent-orange: #ee6c26;
    --rule: #2b2b2b;
    --paper: #ffffff;
  }
  html, body {
    margin: 0;
    padding: 0;
    overflow: hidden;
    background: var(--paper);
  }
  .page {
    position: relative;
    width: 1200px;
    height: 1199px;
    background: var(--paper);
    overflow: hidden;
  }
  .section-title {
    position: absolute;
    left: 110px;
    margin: 0;
    font-family: "Poppins", sans-serif;
    font-weight: 700;
    font-size: 52px;
    line-height: 62px;
    letter-spacing: -0.075em;
    text-transform: uppercase;
    white-space: nowrap;
  }
  .section-title--blue { color: var(--accent-blue); }
  .section-title--orange { color: var(--accent-orange); }
  .section-rule {
    position: absolute;
    left: 484px;
    width: 1.5px;
    background: var(--rule);
  }
  .section-body {
    position: absolute;
    left: 526px;
    width: 600px;
    font-family: "Source Sans 3", sans-serif;
    font-size: 14.2px;
    line-height: 18px;
    color: var(--ink);
  }
  .section-body p {
    margin: 0 0 18px;
  }
</style>
</head>
<body>
<main class="page">

  <section class="proposal-section">
    <h2 class="section-title section-title--blue" style="top:142px;">CEO Massage</h2>
    <div class="section-rule" style="top:133px; height:380px;"></div>
    <div class="section-body" style="top:143px;">
      <p>When you want to get the project approved, you are required to write a project proposal. In this type, you should tell why your project should be approved and what are the potential benefits of the project. The basic objective of every such document is to persuade its reader. If the reader gets impressed, he is likely to accept the proposal.</p>
      <p>The proposed plan to complete the project is the key component of this type. So, the main focus of the reader should be on making a plan and including it.</p>
      <p>When you want to get the project approved, you are required to write a project proposal. In this type, you should tell why your project should be approved and what are the potential benefits of the project. The basic objective of every such document is to persuade its reader. If the reader gets impressed, he is likely to accept the proposal.</p>
      <p>The proposed plan to complete the project is the key component of this type. So, the main focus of the reader should be on making a plan and including it.</p>
    </div>
  </section>

  <section class="proposal-section">
    <h2 class="section-title section-title--orange" style="top:592px;">About Us</h2>
    <div class="section-rule" style="top:583px; height:200px;"></div>
    <div class="section-body" style="top:593px;">
      <p>When you want to get the project approved, you are required to write a project proposal. In this type, you should tell why your project should be approved and what are the potential benefits of the project. The basic objective of every such document is to persuade its reader. If the reader gets impressed, he is likely to accept the proposal.</p>
      <p>The proposed plan to complete the project is the key component of this type. So, the main focus of the reader should be on making a plan and including it.</p>
      <p>When you want to get the project approved, you are required to write a project proposal. In</p>
    </div>
  </section>

  <section class="proposal-section">
    <h2 class="section-title section-title--blue" style="top:876px;">Our<br>Approach</h2>
    <div class="section-rule" style="top:867px; height:200px;"></div>
    <div class="section-body" style="top:877px;">
      <p>When you want to get the project approved, you are required to write a project proposal. In this type, you should tell why your project should be approved and what are the potential benefits of the project. The basic objective of every such document is to persuade its reader. If the reader gets impressed, he is likely to accept the proposal.</p>
      <p>The proposed plan to complete the project is the key component of this type. So, the main focus of the reader should be on making a plan and including it.</p>
      <p>When you want to get the project approved, you are required to write a project proposal. In</p>
    </div>
  </section>

</main>
</body>
</html>
```